Real Estate Open House A Frame Sign

The sign is 22" wide and 28" tall. This sign is used to post around the neighbourhood to direct people to an open house (home that is for sale). It is also used for self-promotion.

Designwise
- I just want something with a modern look, simple and clean.
- I want my picture and business logo on the left side.
- On the right side, website (www.lumwick-realestate.com) and my phone (555-374-9126), then a blank space where I can write an address when I need to.

I'm not sure how I want the overall design look. I'm very open-minded and I'm depending on your creative mind to come up with something.

If you have any questions, please let me know.

```html
<!DOCTYPE html>
<html lang="en">
<head>
<meta charset="utf-8">
<title>Lumwick Real Estate – For Sale Sign</title>
<link href="https://fonts.googleapis.com/css2?family=Montserrat:wght@300;500;700;800&display=swap" rel="stylesheet">
<style>
  :root {
    --brand-blue: #1a4784;
    --stripe-blue: #21508f;
    --ink-gray: #595959;
    --bar-dark: #2a2a2a;
    --white: #ffffff;
    --address-gray: #dcdcdc;
    --page-bg: #f2f2f2;
    --photo-light: #b9bbbe;
    --photo-dark: #6f7277;
  }
  * { margin: 0; padding: 0; box-sizing: border-box; }
  html, body { width: 1200px; height: 795px; overflow: hidden; }
  body {
    background: var(--page-bg);
    font-family: "Montserrat", sans-serif;
    position: relative;
  }
  .sign {
    position: absolute;
    left: 320px; top: 41px;
    width: 560px; height: 713px;
    background: var(--brand-blue);
    overflow: hidden;
  }
  .headline-panel {
    position: absolute;
    left: 15px; top: 19px;
    width: 529px; height: 321px;
    background: var(--white);
    border-radius: 38px 38px 0 0;
    text-align: center;
  }
  .headline-for {
    position: absolute;
    left: 0; right: 0; top: 28px;
    font-weight: 500;
    font-size: 140px;
    line-height: 1;
    color: var(--ink-gray);
    letter-spacing: -2px;
  }
  .headline-sale {
    position: absolute;
    left: 0; right: 0; top: 150px;
    font-weight: 800;
    font-size: 178px;
    line-height: 1;
    color: var(--brand-blue);
    letter-spacing: -5px;
  }
  .brand-block {
    position: absolute;
    left: 0; top: 341px;
    width: 422px; height: 192px;
    background: var(--brand-blue);
    color: var(--white);
    font-weight: 300;
    text-align: center;
  }
  .brand-name {
    position: absolute;
    left: 0; right: 0; top: 42px;
    font-size: 62px;
    line-height: 1;
    letter-spacing: 2px;
  }
  .brand-tagline {
    position: absolute;
    left: 0; right: 0; top: 124px;
    font-size: 26px;
    line-height: 1;
    letter-spacing: 9px;
  }
  .agent-photo {
    position: absolute;
    left: 432px; top: 341px;
    width: 128px; height: 192px;
    background: radial-gradient(ellipse at 45% 35%, var(--photo-light), var(--photo-dark));
  }
  .contact-panel {
    position: absolute;
    left: 15px; top: 544px;
    width: 529px; height: 159px;
    background: var(--white);
    border-radius: 0 0 38px 38px;
  }
  .address-band {
    position: absolute;
    left: 0; top: 544px;
    width: 560px; height: 53px;
    background: rgba(255,255,255,0.94);
    text-align: center;
    font-weight: 800;
    font-size: 31px;
    line-height: 53px;
    color: var(--address-gray);
  }
  .phone-bar {
    position: absolute;
    left: 15px; top: 602px;
    width: 529px; height: 60px;
    background: var(--bar-dark);
    display: flex;
    align-items: center;
    justify-content: center;
    gap: 14px;
  }
  .phone-icon { width: 48px; height: 48px; display: block; }
  .phone-number {
    font-weight: 800;
    font-size: 52px;
    line-height: 1;
    color: var(--white);
    letter-spacing: -1px;
  }
  .website {
    position: absolute;
    left: 15px; top: 666px;
    width: 529px; height: 30px;
    display: flex;
    align-items: center;
    justify-content: center;
    gap: 10px;
    font-weight: 800;
    font-size: 20px;
    color: var(--brand-blue);
  }
  .globe-icon { width: 20px; height: 20px; display: block; }
</style>
</head>
<body>
  <div class="sign">
    <div class="headline-panel">
      <div class="headline-for">FOR</div>
      <div class="headline-sale">SALE</div>
    </div>

    <div class="brand-block">
      <div class="brand-name">LUMWICK</div>
      <div class="brand-tagline">REAL ESTATE</div>
    </div>
    <div class="agent-photo" role="img" aria-label="Portrait photo of the agent in a dark suit, arms crossed, on a grey studio background"></div>

    <div class="contact-panel"></div>
    <div class="address-band">ADDRESS GOES HERE</div>

    <div class="phone-bar">
      <svg class="phone-icon" viewBox="0 0 48 48" aria-hidden="true">
        <circle cx="24" cy="24" r="21" fill="none" stroke="#ffffff" stroke-width="4"/>
        <path d="M17 13c1.5-1 3-1 3.8.6l2 4c.6 1.2.2 2.3-.8 3l-1.4 1c1 2.6 3 4.8 5.6 6l1-1.4c.8-1 1.9-1.3 3-.7l4 2c1.5.8 1.5 2.3.5 3.8-1.4 2-3.6 3-6 2.2-6-2-10.6-6.8-12.5-12.6-.8-2.6.2-4.8 2.1-5.9z" fill="#ffffff"/>
      </svg>
      <span class="phone-number">555-374-9126</span>
    </div>

    <div class="website">
      <svg class="globe-icon" viewBox="0 0 20 20" aria-hidden="true">
        <g fill="none" stroke="#9a9a9a" stroke-width="1.5">
          <circle cx="10" cy="10" r="8.5"/>
          <ellipse cx="10" cy="10" rx="4" ry="8.5"/>
          <line x1="1.5" y1="10" x2="18.5" y2="10"/>
          <line x1="3" y1="5.5" x2="17" y2="5.5"/>
          <line x1="3" y1="14.5" x2="17" y2="14.5"/>
        </g>
      </svg>
      <span>WWW.LUMWICK-REALESTATE.COM</span>
    </div>
  </div>
</body>
</html>
```